Packaging box for giving wine gifts to customers

I need a nice sturdy elegant box to hold one or two bottles of wine that will give to customers as gifts

Designs look the same

```html
<!DOCTYPE html>
<html lang="en">
<head>
<meta charset="utf-8">
<title>KTR Wine Gift Box – Front Panel</title>
<link href="https://fonts.googleapis.com/css2?family=Oswald:wght@400;600&family=Abel&display=swap" rel="stylesheet">
<style>
  :root {
    --page-bg: #ffffff;
    --teal-deep: #0e4d49;
    --teal-mid: #177f7a;
    --teal-bright: #1c9690;
    --teal-base: #157470;
    --ink-light: #ffffff;
    --ink-soft: rgba(255, 255, 255, 0.92);
  }
  html, body {
    margin: 0;
    padding: 0;
    width: 1200px;
    height: 1200px;
    overflow: hidden;
    background: var(--page-bg);
  }
  .canvas {
    position: relative;
    width: 1200px;
    height: 1200px;
  }
  .box-front {
    position: absolute;
    left: 417px;
    top: 60px;
    width: 366px;
    height: 1080px;
    background: linear-gradient(180deg, var(--teal-deep) 0%, var(--teal-mid) 45%, var(--teal-bright) 78%, var(--teal-base) 100%);
    overflow: hidden;
  }
  .circuit-texture {
    position: absolute;
    inset: 0;
    background:
      radial-gradient(ellipse at 30% 25%, rgba(120, 220, 210, 0.10), transparent 60%),
      radial-gradient(ellipse at 70% 80%, rgba(120, 220, 210, 0.12), transparent 60%);
  }
  .brand-block {
    position: absolute;
    left: 0;
    right: 0;
    top: 440px;
    display: flex;
    flex-direction: column;
    align-items: center;
    color: var(--ink-light);
  }
  .brand-name {
    font-family: "Oswald", sans-serif;
    font-weight: 600;
    font-size: 96px;
    line-height: 1;
    letter-spacing: 10px;
    margin: 0;
    padding-left: 10px;
  }
  .brand-rule {
    width: 228px;
    height: 2px;
    background: var(--ink-light);
    margin-top: 12px;
  }
  .brand-tagline {
    font-family: "Oswald", sans-serif;
    font-weight: 400;
    font-size: 15px;
    letter-spacing: 0.4px;
    margin: 8px 0 0;
  }
  .brand-address {
    font-family: "Abel", sans-serif;
    font-size: 17px;
    line-height: 34px;
    margin: 10px 0 0;
    text-align: center;
    color: var(--ink-soft);
  }
  .brand-address .city {
    letter-spacing: 1px;
  }
</style>
</head>
<body>
  <main class="canvas">
    <section class="box-front">
      <div class="circuit-texture" role="img" aria-label="Faint circuit-board trace pattern across the teal panel"></div>
      <div class="brand-block">
        <h1 class="brand-name">KTR</h1>
        <div class="brand-rule"></div>
        <p class="brand-tagline">Printed Circuit Boards Is Our Business</p>
        <p class="brand-address">
          18/F Harbour Plaza, 21 Kestrel Road<br>
          <span class="city">Westwater Bay, HONG KONG</span>
        </p>
      </div>
    </section>
  </main>
</body>
</html>
```